UX Design Document Management App Project

UPDATED PROJECT and INCREASED TOTAL COST. Also added a new design guideline document (4QK - Concept - The Lantern 170613.pdf).

We are a small start-up company based in Sydney, Australia. We have the ideas and coding skills to have built a revolutionary document management app that helps knowledge workers deal with information overload.

We are about to launch an alpha version of a document management app on the iPhone. We have created a series of screens but they lack the brilliance that only a talented graphic designer can deliver. So we would like to find a design partner who can make a contribution in two areas:

1. Make specific changes to our screens such as formatting images so they better blend into the background.
2. Examine our overall UX and either suggest changes or propose new design concepts.
3. Create a logo for this product.

We have completed a pretty comprehensive design brief that we attach to this project and also a set of our existing screen designs in a mix of Photoshop and Keynote formats that we can share with you.

Once we have launched are alpha product, we hope that the winner of this project (our future graphic design partner) will work with us on another project that aims to radically improve the UX of our app in time for a full version 1.0 launch later this year.

We'd like to lock-down the alpha UX in 5 to 10 days but if the ideas you have are exciting enough we can extend this time.
Updates

Project now has a SIGNIFICANTLY INCREASED BUDGET (almost doubled) and an expanded scope to deliver a logo for our product. Check out the additional design brief document just uploaded.

Hello Designers,

Just to let you know that we have updated the project and INCREASED THE TOTAL BUDGET. We have also added a new design guideline document (4QK - Concept - The Lantern 170613.pdf) to help inspire you!

The project now has a significantly increased budget (almost doubled) and an expanded scope to also deliver a logo for our Mollant product. Check out the additional design brief document just uploaded.

Thanks for participating!

All the best,

Gareth

Barring any unforeseen circumstances, this design competition will remain open until midnight Pacific Standard Time this Sunday. That means about 10 am Sydney time this Monday, July 1st. Good luck and get your designs in!

Project Deadline Extended
Reason: I agreed to use PST not AEST!

Target Market(s)

individual knowledge workers: professionals, office workers/managers, university students, academics/researchers, etc.

Industry/Entity Type

Graphic Designer

Requirements
Must have
• professional, highly effective UX

```html
<!DOCTYPE html>
<html lang="en">
<head>
<meta charset="utf-8">
<title>Mollant – Launch Screen</title>
<link rel="stylesheet" href="https://fonts.googleapis.com/css2?family=Heebo:wght@200;300;400;600&display=swap">
<style>
  :root {
    --page-bg: #0d1a2c;
    --screen-bg: #0a0a0a;
    --status-bg: #e9e9e9;
    --status-text: #1a1a1a;
    --photo-light: #9a9a9a;
    --photo-mid: #5c5c5c;
    --photo-deep: #333333;
    --photo-dark: #141414;
    --brand-panel: rgba(26, 26, 26, 0.85);
    --brand-blue: #1e7fd6;
    --tagline-text: #f2f2f2;
    --accent-green: #8ee000;
    --accent-green-text: #2b4a00;
  }
  * { box-sizing: border-box; margin: 0; padding: 0; }
  html, body {
    width: 1200px;
    height: 1040px;
    overflow: hidden;
    background: var(--page-bg);
    font-family: "Heebo", "Helvetica Neue", Arial, sans-serif;
  }
  .app-screen {
    position: absolute;
    left: 307px;
    top: 0;
    width: 586px;
    height: 1040px;
    background: var(--screen-bg);
    overflow: hidden;
  }
  .status-bar {
    position: absolute;
    inset: 0 0 auto 0;
    height: 34px;
    background: var(--status-bg);
    color: var(--status-text);
    font-size: 18px;
    display: flex;
    align-items: center;
    justify-content: space-between;
    padding: 0 16px;
    z-index: 2;
  }
  .status-bar .carrier { display: flex; align-items: center; gap: 8px; }
  .status-bar .time { font-weight: 600; position: absolute; left: 50%; transform: translateX(-50%); }
  .status-bar .battery { display: flex; align-items: center; gap: 8px; }
  .hero-photo {
    position: absolute;
    left: 0; top: 34px;
    width: 100%;
    height: 1006px;
    background:
      radial-gradient(ellipse 70% 45% at 50% 8%, rgba(170,170,170,0.55) 0%, rgba(170,170,170,0) 100%),
      linear-gradient(180deg, var(--photo-light) 0%, var(--photo-mid) 30%, var(--photo-deep) 60%, var(--photo-dark) 82%, var(--screen-bg) 100%);
  }
  .brand-panel {
    position: absolute;
    left: 101px;
    top: 260px;
    width: 324px;
    height: 297px;
    background: var(--brand-panel);
  }
  .brand-mark {
    position: absolute;
    left: 50%;
    top: 88px;
    width: 40px;
    height: 40px;
    margin-left: -20px;
    background: var(--brand-blue);
  }
  .brand-name {
    position: absolute;
    left: 0;
    right: 0;
    top: 180px;
    text-align: center;
    color: var(--brand-blue);
    font-weight: 300;
    font-size: 62px;
    letter-spacing: 1px;
    line-height: 64px;
  }
  .tagline {
    position: absolute;
    left: 56px;
    top: 861px;
    height: 87px;
    display: flex;
    align-items: center;
    gap: 22px;
  }
  .tagline-label {
    color: var(--tagline-text);
    font-weight: 200;
    font-size: 40px;
  }
  .tagline-badge {
    width: 253px;
    height: 87px;
    border-radius: 6px;
    background: var(--accent-green);
    color: var(--accent-green-text);
    font-weight: 200;
    font-size: 40px;
    display: flex;
    align-items: center;
    justify-content: center;
  }
</style>
</head>
<body>
  <main class="app-screen">
    <header class="status-bar">
      <span class="carrier">
        <svg width="44" height="10" viewBox="0 0 44 10" aria-hidden="true">
          <circle cx="5" cy="5" r="4" fill="#1a1a1a"/>
          <circle cx="14" cy="5" r="4" fill="#1a1a1a"/>
          <circle cx="23" cy="5" r="4" fill="none" stroke="#1a1a1a"/>
          <circle cx="32" cy="5" r="4" fill="none" stroke="#1a1a1a"/>
          <circle cx="41" cy="5" r="2.5" fill="none" stroke="#1a1a1a"/>
        </svg>
        Operator
        <svg width="20" height="14" viewBox="0 0 20 14" aria-hidden="true">
          <path d="M10 13 L6 9 A6 6 0 0 1 14 9 Z" fill="#1a1a1a"/>
          <path d="M3 6 A10 10 0 0 1 17 6" fill="none" stroke="#1a1a1a" stroke-width="2"/>
          <path d="M0.5 3 A14 14 0 0 1 19.5 3" fill="none" stroke="#1a1a1a" stroke-width="2"/>
        </svg>
      </span>
      <span class="time">11:27 AM</span>
      <span class="battery">
        100 %
        <svg width="40" height="16" viewBox="0 0 40 16" aria-hidden="true">
          <rect x="1" y="1" width="34" height="14" rx="2" fill="none" stroke="#1a1a1a" stroke-width="1.5"/>
          <rect x="3" y="3" width="30" height="10" fill="#1a1a1a"/>
          <rect x="36" y="5" width="3" height="6" fill="#1a1a1a"/>
        </svg>
      </span>
    </header>

    <div class="hero-photo" role="img" aria-label="Black and white photograph looking up through the steel girders of a large arch bridge, fading to black at the bottom"></div>

    <section class="brand-panel">
      <span class="brand-mark" aria-hidden="true"></span>
      <h1 class="brand-name">MOLLANT</h1>
    </section>

    <p class="tagline">
      <span class="tagline-label">Documents:</span>
      <span class="tagline-badge">Reinvented.</span>
    </p>
  </main>
</body>
</html>
```